Fiber Optic Internet flyer promotion Winter 2016-2017

I am looking for a marketing flyer that will not be folded, single sided that will advertise a Fiber Optic internet promotion that we are currently running.

The design should be clean, flow well, quickly grab attention, and if a very few short seconds list what the promotion is, and direct them to contact us.

It needs to list a few features of the promotion, but does not need to be in this order and should flow well with the flyer
1.) Fiber Optic Internet
2.) 100 Mbits for $140 /month or 150 Mbits for $190 /month
3.) Free construction cost up to $10,000, limited funds available.
4.) Limited time offer. Must commit before funds run out.

(555) 274-3619, www.kelvaroute.net

Target Market(s)

Small to large business

Industry/Entity Type

Internet Service Provider

Requirements
Must have
• Eye catching appeal. Quickly convey the message of the promotion and our company name and phone number.
Should not have
• Our company is primarily a wireless ISP. This promotion is all about Fiber Optic. I do not want to draw attention to the "wireless" portion of our business with this flyer.

```html
<!DOCTYPE html>
<html lang="en">
<head>
<meta charset="utf-8">
<title>Fiber Optic Internet – Winter Promotion</title>
<link rel="stylesheet" href="https://fonts.googleapis.com/css2?family=Bebas+Neue&family=Oswald:wght@300;400;500;700&display=swap">
<style>
  :root {
    --navy: #232a6b;
    --red: #e3202b;
    --red-dark: #b8141d;
    --red-deep: #8e0f16;
    --badge-light: #f2f2f2;
    --badge-mid: #d4d4d4;
    --ink: #2b2b2b;
    --sky-top: #5fb0c8;
    --sky-bottom: #b9dfe9;
    --snow: #f6f8fa;
    --white: #ffffff;
  }
  * { box-sizing: border-box; margin: 0; padding: 0; }
  html, body { width: 790px; height: 1200px; overflow: hidden; background: var(--white); }
  .flyer {
    position: relative; width: 790px; height: 1200px; overflow: hidden;
    background: var(--white);
    font-family: "Oswald", sans-serif;
  }
  .photo {
    position: absolute; left: 0; top: 0; width: 790px; height: 520px;
    background:
      radial-gradient(ellipse 260px 300px at 570px 270px, #c8262e 0%, #c8262e 35%, rgba(200,38,46,0) 70%),
      radial-gradient(ellipse 120px 150px at 560px 120px, #6a4330 0%, rgba(106,67,48,0) 80%),
      linear-gradient(90deg, #ffffff 0%, #f4f1ec 35%, #d9cfc3 70%, #c9b9a6 100%);
  }
  .scene {
    position: absolute; left: 0; top: 690px; width: 790px; height: 510px;
    background:
      radial-gradient(ellipse 700px 220px at 400px 520px, var(--snow) 0%, var(--snow) 55%, rgba(246,248,250,0) 100%),
      linear-gradient(180deg, var(--sky-top) 0%, var(--sky-bottom) 70%, var(--snow) 100%);
  }
  .bands { position: absolute; left: 0; top: 0; width: 790px; height: 1200px; }
  .brand {
    position: absolute; left: 0; top: 70px; width: 340px;
    display: flex; align-items: center; justify-content: center; gap: 10px;
    font-family: "Oswald", sans-serif; font-weight: 700; font-size: 24px;
    color: var(--navy); letter-spacing: 1px;
  }
  .brand-dot { width: 16px; height: 16px; border-radius: 50%; background: var(--red); }
  .headline {
    position: absolute; left: 48px; top: 222px;
    font-family: "Bebas Neue", sans-serif; line-height: 1;
  }
  .headline .line-fiber { display: block; font-size: 78px; color: var(--navy); }
  .headline .line-internet { display: block; font-size: 94px; color: var(--red); margin-top: 4px; }
  .pricing {
    position: absolute; left: 470px; top: 535px; width: 310px;
    text-align: center; color: var(--white); font-weight: 300; font-size: 30px; line-height: 1.22;
  }
  .badge {
    position: absolute; left: 48px; top: 478px; width: 300px; height: 300px; border-radius: 50%;
    background: radial-gradient(circle at 50% 40%, var(--badge-light) 0%, var(--badge-mid) 100%);
    border: 6px solid rgba(255,255,255,0.85);
    box-shadow: 0 4px 14px rgba(0,0,0,0.25);
    text-align: center; padding-top: 48px;
  }
  .badge .limited { display: block; font-family: "Bebas Neue", sans-serif; font-size: 80px; line-height: 0.9; color: var(--red); }
  .badge .offer { display: block; font-family: "Bebas Neue", sans-serif; font-size: 56px; line-height: 1; color: var(--red); }
  .badge .commit { display: block; font-size: 27px; font-weight: 400; line-height: 1.25; color: var(--ink); margin-top: 4px; }
  .construction {
    position: absolute; right: 78px; top: 800px; text-align: right;
    font-size: 35px; font-weight: 300; line-height: 1.45;
  }
  .construction .lead { display: block; color: var(--navy); }
  .construction .lead strong { font-weight: 500; }
  .construction .limit { display: block; color: var(--red); }
  .season {
    position: absolute; left: 251px; top: 954px;
    font-size: 33px; font-weight: 300; color: var(--red);
  }
  .hours {
    position: absolute; right: 17px; top: 1104px; width: 430px; text-align: right;
    font-size: 10.5px; line-height: 1.55; color: var(--ink);
  }
  .phone {
    position: absolute; right: 17px; top: 1140px;
    display: flex; align-items: center; gap: 10px;
    font-size: 32px; font-weight: 500; color: var(--red);
  }
  .phone svg { width: 28px; height: 22px; }
  .web {
    position: absolute; left: 40px; top: 1160px;
    display: flex; align-items: center; gap: 8px;
    font-size: 19px; color: var(--red);
  }
  .web-dot { width: 10px; height: 10px; border-radius: 50%; background: var(--navy); }
</style>
</head>
<body>
<main class="flyer">
  <div class="photo" role="img" aria-label="Photo of a smiling woman in a red coat looking at her smartphone on a sunny street"></div>
  <div class="scene" role="img" aria-label="Winter illustration with falling snow, a snowman, pine trees and a snowy log cabin"></div>

  <svg class="bands" viewBox="0 0 790 1200" aria-hidden="true">
    <polygon points="0,478 790,455 790,770 380,705 0,565" fill="var(--red)"/>
    <polygon points="300,600 790,455 790,620" fill="var(--red-dark)"/>
    <polygon points="420,540 790,455 790,500" fill="var(--red-deep)" opacity="0.6"/>
    <polygon points="0,565 380,705 0,790" fill="var(--navy)"/>
    <polygon points="380,705 790,770 790,790 420,725" fill="var(--red-dark)" opacity="0.7"/>
  </svg>

  <div class="brand"><span class="brand-dot"></span>MESA RIDGE NETWORKS</div>

  <h1 class="headline">
    <span class="line-fiber">FIBER OPTIC</span>
    <span class="line-internet">INTERNET</span>
  </h1>

  <p class="pricing">100 Mbits for $140 /month<br>or<br>150 Mbits for $190 /month</p>

  <div class="badge">
    <span class="limited">LIMITED</span>
    <span class="offer">TIME OFFER.</span>
    <span class="commit">Must commit before<br>funds run out</span>
  </div>

  <p class="construction">
    <span class="lead">Free construction cost up to <strong>$10,000,</strong></span>
    <span class="limit">limited funds available.</span>
  </p>

  <p class="season">Winter 2016-2017</p>

  <p class="hours">Please feel free to call us during these hours to speak with a staff member, or<br>you can leave a message that will be returned as early as possible the next business day.</p>

  <p class="phone">
    <svg viewBox="0 0 28 22" aria-hidden="true">
      <path d="M2 8 Q14 -2 26 8 L22 11 L19 8 Q14 5 9 8 L6 11 Z" fill="var(--navy)"/>
      <rect x="7" y="11" width="14" height="9" rx="2" fill="var(--navy)"/>
      <circle cx="14" cy="15.5" r="2.5" fill="var(--white)"/>
    </svg>
    (555) 274-3619
  </p>

  <p class="web"><span class="web-dot"></span>www.kelvaroute.net</p>
</main>
</body>
</html>
```